Travel Company is looking for a STAND OUT Business Card

I need a unique Business Card that will truly stand out. Nothing too busy. Simple is good, right? Not looking for a standard design either. No cookie cutter layout. We are a Travel Company that works more with Companies than Travelers. I had an idea to focus and emphasis on the 2 logo a bit more. This is not necessary, however thought it would look interesting. I am just looking for something interesting and a bit different. Does't have to completely off the wall crazy, just not your run of the mill business card.

Target Market(s)

Hoteliers, Resort Management, Call Centers, Executives, Travelers, Families, Businesses

Industry/Entity Type

Hospitality

Contact Information for Business Card

President/CEO - Marcus T Bellamy (title not necessary if design doesn't allow for it)
contact - (407) 555-0186
email - mbellamy@wayfarenow.example
address - 4812 Quillmore Ave #164
Orlando, FL 32804
website - www.wayfarenow.example

Font styles to use
Serif
Other font styles liked:
• Avenir Next LT Pro BOLD

Requirements
Must have
• simple look and design. Unique design
Nice to have
• I attached the 2 logo separate from the main logo. This can be used separately from the Main Logo, together with the main logo or as main logo. I included the logo font. Use it or not, designers choice.
Should not have
• cookie cutter design. Little use of red other than the logo

```html
<!DOCTYPE html>
<html lang="en">
<head>
<meta charset="utf-8">
<title>Wayfarenow Business Card</title>
<link rel="stylesheet" href="https://fonts.googleapis.com/css2?family=Montserrat:wght@500;600;800&display=swap">
<style>
  :root {
    --stage: #ecebe8;
    --card-white: #ffffff;
    --card-black: #0b0b0b;
    --ink: #1b1b1b;
    --ink-soft: #4a4a4a;
    --arc-dark: #2a2a2a;
    --brand-red: #e3101a;
    --brand-red-deep: #b80d14;
  }
  * { box-sizing: border-box; margin: 0; padding: 0; }
  html, body {
    width: 1200px; height: 950px; overflow: hidden;
    background: var(--stage);
    font-family: "Montserrat", Arial, sans-serif;
  }
  .stage { position: relative; width: 1200px; height: 950px; }

  .card {
    position: absolute; top: 150px;
    width: 380px; height: 650px;
    border-radius: 6px; overflow: hidden;
    box-shadow: 0 14px 34px rgba(0,0,0,0.18);
  }
  .card-front { left: 180px; background: var(--card-white); }
  .card-back  { left: 640px; background: var(--card-black); }

  .front-graphic { position: absolute; inset: 0; }

  .wordmark {
    position: absolute; left: 0; right: 0;
    text-align: center;
    font-weight: 800; letter-spacing: -1px;
  }
  .card-front .wordmark { top: 82px; font-size: 50px; color: var(--ink); }
  .card-back .wordmark  { top: 296px; font-size: 50px; color: #ffffff; }

  .contact {
    position: absolute; left: 92px; top: 300px;
    color: var(--ink-soft); font-size: 14px; line-height: 1.55; font-weight: 500;
  }
  .contact .name { color: var(--brand-red); font-size: 20px; font-weight: 600; line-height: 1.2; }
  .contact .title { color: var(--ink); font-size: 14px; margin-bottom: 12px; }
  .contact .label { color: var(--brand-red); font-weight: 600; }
</style>
</head>
<body>
<main class="stage">
  <section class="card card-front" aria-label="Card front">
    <svg class="front-graphic" width="380" height="650" viewBox="0 0 380 650">
      <defs>
        <linearGradient id="redFade" x1="0" y1="0" x2="0" y2="1">
          <stop offset="0" stop-color="#ff2a30"/>
          <stop offset="1" stop-color="#b80d14"/>
        </linearGradient>
      </defs>
      <rect x="0" y="470" width="380" height="180" fill="url(#redFade)"/>
      <circle cx="200" cy="370" r="176" fill="#ffffff"/>
      <path d="M 40 300 A 176 176 0 0 1 360 300" fill="none" stroke="var(--arc-dark)" stroke-width="16" stroke-linecap="butt"/>
      <path d="M 50 470 A 176 176 0 0 0 350 470" fill="none" stroke="var(--brand-red)" stroke-width="16"/>
    </svg>
    <div class="wordmark">wayfarenow</div>
    <div class="contact">
      <p class="name">Marcus T Bellamy</p>
      <p class="title">President/CEO</p>
      <p>4812 Quillmore Ave #164</p>
      <p>Orlando, FL 32804</p>
      <p><span class="label">P :</span> (407) 555-0186</p>
      <p><span class="label">E :</span> mbellamy@wayfarenow.example</p>
      <p><span class="label">W :</span> www.wayfarenow.example</p>
    </div>
  </section>

  <section class="card card-back" aria-label="Card back">
    <div class="wordmark">wayfarenow</div>
  </section>
</main>
</body>
</html>
```